Modernise Business Card

Our company has been operating for 10 years. With the start of the new decade we are looking to refresh our business card design. We manufacture a range of industrial product shipping to customers internationally. A copy of our current card, both sides, is attached. We are looking for a mature professional appearance.

```html
<!DOCTYPE html>
<html lang="en">
<head>
<meta charset="utf-8">
<title>Norvane Business Card</title>
<link rel="stylesheet" href="https://fonts.googleapis.com/css2?family=Lato:wght@400;700;900&display=swap">
<style>
  :root {
    --bg: #d9d9d9;
    --paper: #ffffff;
    --blue: #2398d4;
    --blue-light: #33bde6;
    --blue-deep: #1e8ccc;
    --ink: #1c1c1c;
    --line: #222222;
  }
  * { margin: 0; padding: 0; box-sizing: border-box; }
  html, body { width: 1200px; height: 900px; overflow: hidden; }
  body {
    background: var(--bg);
    font-family: "Lato", sans-serif;
    position: relative;
  }
  .card {
    position: absolute;
    width: 560px;
    height: 320px;
    background: var(--paper);
    overflow: hidden;
    box-shadow: 0 6px 18px rgba(0,0,0,0.18);
  }
  .card-art { position: absolute; inset: 0; width: 100%; height: 100%; }
  .card-front { left: 80px; top: 110px; }
  .card-back { left: 560px; top: 470px; }

  .brand {
    position: absolute;
    display: flex;
    align-items: center;
    gap: 10px;
    font-weight: 900;
    color: var(--blue);
    letter-spacing: -0.5px;
    line-height: 1;
  }
  .brand-mark {
    width: 14px; height: 14px;
    background: var(--blue);
  }
  .card-front .brand { left: 165px; top: 48px; font-size: 54px; }
  .card-front .brand-mark { width: 18px; height: 18px; }

  .tagline {
    position: absolute;
    left: 232px; top: 222px;
    color: var(--paper);
    font-size: 15px;
    letter-spacing: 2.5px;
    line-height: 1.4;
    text-transform: uppercase;
  }
  .front-web {
    position: absolute;
    left: 262px; top: 280px;
    color: var(--paper);
    font-weight: 700;
    font-size: 15px;
    letter-spacing: 1.5px;
  }

  .card-back .brand { left: 36px; top: 34px; font-size: 40px; }
  .holder-name {
    position: absolute; left: 40px; top: 92px;
    font-size: 23px; font-weight: 400; color: var(--ink);
  }
  .phones {
    position: absolute; left: 40px; top: 140px;
    font-size: 13px; color: var(--ink); line-height: 1.35;
  }
  .links {
    position: absolute; left: 40px; top: 188px;
    list-style: none; font-size: 15px; color: var(--ink); line-height: 1.5;
  }
  .links li { display: flex; align-items: center; gap: 6px; }
  .links svg { width: 13px; height: 13px; }
  .address {
    position: absolute; left: 40px; top: 246px;
    font-style: normal; font-weight: 700; font-size: 14px;
    color: var(--blue); line-height: 1.35;
  }
</style>
</head>
<body>

<section class="card card-front" aria-label="Card front">
  <svg class="card-art" viewBox="0 0 560 320" aria-hidden="true">
    <defs>
      <radialGradient id="frontBlue" cx="0.6" cy="0.6" r="0.7">
        <stop offset="0" stop-color="var(--blue-light)"/>
        <stop offset="1" stop-color="var(--blue)"/>
      </radialGradient>
    </defs>
    <path d="M0 275 C200 255 380 150 560 45 L560 320 L0 320 Z" fill="url(#frontBlue)"/>
    <path d="M0 275 C200 255 380 150 560 45" fill="none" stroke="var(--line)" stroke-width="4"/>
  </svg>
  <div class="brand"><span class="brand-mark"></span>Norvane</div>
  <p class="tagline">Hydrulicadapters hose<br>fittings quick couplings</p>
  <p class="front-web">www.norvanefittings.com</p>
</section>

<section class="card card-back" aria-label="Card back">
  <svg class="card-art" viewBox="0 0 560 320" aria-hidden="true">
    <defs>
      <linearGradient id="backBlue" x1="0" y1="0" x2="0" y2="1">
        <stop offset="0" stop-color="var(--blue-deep)"/>
        <stop offset="1" stop-color="var(--blue-light)"/>
      </linearGradient>
    </defs>
    <path d="M375 0 C440 80 450 220 415 320 L560 320 L560 0 Z" fill="url(#backBlue)"/>
    <path d="M368 -2 C433 80 443 220 408 322" fill="none" stroke="var(--line)" stroke-width="6"/>
  </svg>
  <div class="brand"><span class="brand-mark"></span>Norvane</div>
  <h1 class="holder-name">Peter Hallam</h1>
  <p class="phones">China: +86 100 5550 0147<br>Australia: + 61 400 555 018</p>
  <ul class="links">
    <li><svg viewBox="0 0 14 14" aria-hidden="true"><circle cx="7" cy="7" r="6" fill="none" stroke="var(--ink)" stroke-width="1.4"/><path d="M1 7h12M7 1c-3 3-3 9 0 12M7 1c3 3 3 9 0 12" fill="none" stroke="var(--ink)" stroke-width="1"/></svg>www.norvanefittings.com</li>
    <li><svg viewBox="0 0 14 14" aria-hidden="true"><circle cx="7" cy="7" r="6.5" fill="var(--ink)"/><rect x="3.5" y="4.5" width="7" height="5" fill="none" stroke="#fff" stroke-width="1"/><path d="M3.5 4.5 7 7.5 10.5 4.5" fill="none" stroke="#fff" stroke-width="1"/></svg>phallam@norvanefittings.com</li>
  </ul>
  <address class="address">Address: 1208 Harbour View Building<br>88 Example Road.Eastside.District<br>Ningbo 315000 China</address>
</section>

</body>
</html>
```